Should your crown slip dance anyway! book cover design

Book cover for a business, non-fiction book.
About stepping up, being who you truly are, and willing not to fit in.

TITLE: Should Your Crown Slip, Dance Anyway!
SUBTITLE: Stop being the leader you think you should be and start becoming the leader that only you can be...
AUTHOR: Rowan Haddleworth-Bligh
Updates

we never uploaded the brief

Target Market(s)

Business people, curious leaders, insiders who have a secret itch to be an outsider
AGE: 35-50 years old

Font styles to use
Sans Serif
Other font styles liked:
• designer's choice!

Requirements
Must have
• Very visual
Imagery must reflect the topic of the book

```html
<!DOCTYPE html>
<html lang="en">
<head>
<meta charset="utf-8">
<title>Should Your Crown Slip, Dance Anyway! — Book Cover</title>
<link rel="stylesheet" href="https://fonts.googleapis.com/css2?family=Tinos:wght@700&family=Montserrat:wght@400&family=Cinzel:wght@400&display=swap">
<style>
  :root {
    --backdrop: #c4c4c4;
    --paper: #ededed;
    --navy: #060a3a;
    --title-navy: #0b1a4f;
    --title-red: #e3070b;
    --window-light: #f6f7f1;
    --window-haze: #dde3e4;
    --table-glow: #7fa3b8;
    --room-blue: #2a3a66;
    --ink-light: #f2f3f7;
  }
  * { margin: 0; padding: 0; box-sizing: border-box; }
  html, body { width: 1200px; height: 800px; overflow: hidden; }
  body {
    background: var(--backdrop);
    display: flex;
    align-items: center;
    justify-content: center;
  }
  .book-cover {
    position: relative;
    width: 470px;
    height: 720px;
    background: var(--paper);
    overflow: hidden;
  }
  .cover-photo {
    position: absolute;
    left: 0;
    top: 211px;
    width: 100%;
    height: 301px;
    background:
      radial-gradient(ellipse 55% 38% at 50% 82%, rgba(127,163,184,0.85) 0%, rgba(127,163,184,0) 100%),
      radial-gradient(ellipse 60% 55% at 50% 40%, var(--window-light) 0%, rgba(246,247,241,0) 100%),
      linear-gradient(90deg, rgba(150,160,165,0.35) 0%, rgba(150,160,165,0) 18%, rgba(150,160,165,0) 82%, rgba(150,160,165,0.35) 100%),
      linear-gradient(180deg,
        var(--window-haze) 0%,
        #eceeea 35%,
        #e2e8e8 52%,
        #b9c8d1 56%,
        #4a5d82 62%,
        var(--room-blue) 72%,
        #1c2752 88%,
        var(--navy) 100%);
  }
  .lower-band {
    position: absolute;
    left: 0;
    top: 512px;
    width: 100%;
    height: 208px;
    background: var(--navy);
  }
  .title {
    position: absolute;
    left: 0;
    top: 44px;
    width: 100%;
    text-align: center;
    font-family: "Tinos", "Times New Roman", serif;
    font-weight: 700;
    text-transform: uppercase;
    z-index: 1;
  }
  .title-line {
    display: block;
    color: var(--title-navy);
    font-size: 50px;
    line-height: 80px;
    height: 80px;
    white-space: nowrap;
  }
  .title-line--accent {
    color: var(--title-red);
    font-size: 46px;
    margin-top: -1px;
  }
  .subtitle {
    position: absolute;
    left: 0;
    top: 528px;
    width: 100%;
    text-align: center;
    font-family: "Montserrat", Arial, sans-serif;
    font-weight: 400;
    font-size: 19.5px;
    line-height: 24.5px;
    color: var(--ink-light);
    text-transform: uppercase;
    white-space: nowrap;
  }
  .author {
    position: absolute;
    left: 0;
    top: 668px;
    width: 100%;
    text-align: center;
    font-family: "Cinzel", "Times New Roman", serif;
    font-size: 19.5px;
    letter-spacing: 3px;
    color: var(--ink-light);
    text-transform: uppercase;
    white-space: nowrap;
  }
</style>
</head>
<body>
  <main class="book-cover">
    <div class="cover-photo" role="img" aria-label="Photograph of a leader standing and presenting to a team seated around a boardroom table, backlit by bright floor-to-ceiling windows"></div>
    <div class="lower-band"></div>
    <h1 class="title">
      <span class="title-line">Should Your</span>
      <span class="title-line">Crown Slip,</span>
      <span class="title-line title-line--accent">Dance Anyway!</span>
    </h1>
    <p class="subtitle">Stop being the leader you<br>think you should be and<br>start becoming the leader<br>that only you can be...</p>
    <p class="author">Rowan Haddleworth-Bligh</p>
  </main>
</body>
</html>
```